Individual Brochures for 6 products

Urgent request need this in 2 days thank you.

I need 2 fold Brochure (W:20XH:23) simple brochures (individual) for 6 products the overall look is white, clean with a touch of metalic red and black. I included photos of each products and description in folder. This is for Medical Clinic so make the design more medical and clean

files can be found from dropbox link below

https://www.filecrate.example/sh/7pq83wxmrhnalf/BBD2KTRuPsMNG_QxLnNzWpRkb?dl=0

Note: file i have attach below is size i want for the brochure. The design and photos are on the dropbox link above.

Thank you in advance for rushing this project

Target Market(s)

Aesthetic, beauty industry

Industry/Entity Type

Medical

Other font styles liked:
• Velsa - Roboto, ORT- Bangla MN

Colors
ffffff
ec1f27

Requirements
Must have
• photo of a lady in each brochures (different product different photos) see photos in dropbox link
• https://www.filecrate.example/sh/m9r461vtbk537zy/BBD_wuhLQZnfpT2HkJ6RsNbVe?dl=0

```html
<!DOCTYPE html>
<html lang="en">
<head>
<meta charset="utf-8">
<title>Velsa Medi-Skincare – Brochure Spread</title>
<link rel="stylesheet" href="https://fonts.googleapis.com/css2?family=Cinzel:wght@400&family=PT+Sans:wght@400;700&display=swap">
<style>
  :root {
    --stage: #333436;
    --paper: #ffffff;
    --paper-shade: #e9e9ea;
    --red: #ec1f27;
    --red-deep: #b50d16;
    --ink: #222222;
    --pink-soft: #e8d2dc;
  }
  * { margin: 0; padding: 0; box-sizing: border-box; }
  html, body { width: 973px; height: 1200px; overflow: hidden; background: var(--stage); }
  .stage { position: relative; width: 973px; height: 1200px; }
  .spread {
    position: absolute; left: 36px; top: 282px;
    width: 820px; height: 580px;
    transform: scale(1.0976); transform-origin: 0 0;
    overflow: hidden;
    box-shadow: 0 10px 30px rgba(0,0,0,.5);
  }
  .panel { position: absolute; top: 0; height: 580px; width: 410px; }
  .panel--back { left: 0; background: linear-gradient(90deg, #fbfbfb 0%, #f6f6f6 70%, var(--paper-shade) 100%); }
  .panel--front { left: 410px; background: linear-gradient(180deg, #fafafb 0%, #f1f0f3 60%, #e8e7ea 100%); }
  .photo {
    position: absolute; left: 590px; top: 0; width: 230px; height: 470px;
    background: radial-gradient(ellipse at 62% 48%, #e3c3b4 0%, #ead7d9 35%, var(--pink-soft) 60%, rgba(240,238,242,0) 100%);
  }
  .waves { position: absolute; left: 0; top: 0; width: 820px; height: 580px; }
  .wordmark {
    position: absolute;
    font-family: "PT Sans", sans-serif; font-weight: 400; color: var(--ink);
    letter-spacing: 1px; line-height: 1;
  }
  .wordmark--back { left: 150px; top: 236px; font-size: 38px; }
  .wordmark--front { left: 437px; top: 50px; font-size: 46px; }
  .headline {
    position: absolute; left: 439px; top: 228px;
    font-family: "Cinzel", serif; font-weight: 400; font-size: 20px; line-height: 24px;
    color: var(--red-deep); letter-spacing: .5px;
  }
  .contact-title {
    position: absolute; left: 0; width: 410px; top: 500px; text-align: center;
    font-family: "PT Sans", sans-serif; font-size: 14px; color: var(--paper);
  }
  .contact-item {
    position: absolute; display: flex; align-items: flex-start; gap: 5px;
    font-family: "PT Sans", sans-serif; font-size: 10px; line-height: 12px; color: var(--paper);
  }
  .contact-item svg { flex: none; margin-top: 2px; }
  .contact-item--address { left: 20px; top: 538px; }
  .contact-item--phone { left: 163px; top: 544px; align-items: center; }
  .contact-item--phone svg { margin-top: 0; }
  .contact-list { position: absolute; left: 265px; top: 537px; }
  .contact-list .contact-item { position: static; }
  .offer {
    position: absolute; left: 420px; width: 390px; top: 502px; text-align: center;
    font-family: "PT Sans", sans-serif; font-weight: 700; font-size: 13.5px; line-height: 16px; color: var(--paper);
  }
  .web-pill {
    position: absolute; left: 544px; top: 562px; width: 143px; height: 24px;
    background: var(--paper); border-radius: 7px; text-align: center;
    font-family: "Cinzel", serif; font-size: 10.5px; line-height: 18px; color: var(--red-deep);
  }
</style>
</head>
<body>
<div class="stage">
  <div class="spread">
    <div class="panel panel--back"></div>
    <div class="panel panel--front"></div>
    <div class="photo" role="img" aria-label="Photo of a woman in profile with pink magnolia blossoms against a soft bokeh background"></div>

    <svg class="waves" viewBox="0 0 820 580" aria-hidden="true">
      <defs>
        <linearGradient id="silverBand" x1="0" y1="0" x2="1" y2="0">
          <stop offset="0" stop-color="#8e8e90"/>
          <stop offset=".35" stop-color="#d8d8da"/>
          <stop offset=".7" stop-color="#9c9c9e"/>
          <stop offset="1" stop-color="#d2d2d4"/>
        </linearGradient>
        <linearGradient id="redBand" x1="0" y1="0" x2="1" y2="1">
          <stop offset="0" stop-color="#e31b23"/>
          <stop offset=".5" stop-color="#c8101a"/>
          <stop offset="1" stop-color="#d5161f"/>
        </linearGradient>
      </defs>
      <path d="M0,440 C120,402 230,378 330,392 C450,410 560,466 700,464 C760,463 800,438 820,422 L820,580 L0,580Z" fill="url(#silverBand)"/>
      <path d="M0,456 C120,418 230,398 330,410 C450,426 560,480 700,478 C760,477 800,456 820,442 L820,580 L0,580Z" fill="#ffffff"/>
      <path d="M0,460 C120,422 230,402 330,414 C450,430 560,484 700,482 C760,481 800,460 820,446 L820,580 L0,580Z" fill="url(#redBand)"/>
      <line x1="410" y1="0" x2="410" y2="580" stroke="rgba(0,0,0,.06)" stroke-width="1"/>
    </svg>

    <div class="wordmark wordmark--back">Velsa</div>

    <div class="contact-title">CONTACT US TODAY</div>
    <div class="contact-item contact-item--address">
      <svg width="6" height="8" viewBox="0 0 6 8"><path d="M3 0a3 3 0 0 1 3 3c0 2-3 5-3 5S0 5 0 3a3 3 0 0 1 3-3z" fill="#fff"/><circle cx="3" cy="3" r="1" fill="#d5161f"/></svg>
      <span>214 N. Carrow St.<br>Alden Falls, PA 18099</span>
    </div>
    <div class="contact-item contact-item--phone">
      <svg width="9" height="7" viewBox="0 0 9 7"><path d="M0 2c2-2 7-2 9 0v1.5H6.5V2.5h-4v1H0z M2 4h5l1 3H1z" fill="#fff"/></svg>
      <span>555-010-246</span>
    </div>
    <div class="contact-list">
      <div class="contact-item">
        <svg width="8" height="6" viewBox="0 0 8 6"><rect width="8" height="6" fill="#fff"/><path d="M0 0l4 3 4-3" stroke="#d5161f" fill="none" stroke-width=".8"/></svg>
        <span>info@velsa.example</span>
      </div>
      <div class="contact-item">
        <svg width="7" height="7" viewBox="0 0 7 7"><circle cx="3.5" cy="3.5" r="3.5" fill="#fff"/><circle cx="3.5" cy="3.5" r="1.4" fill="#d5161f"/></svg>
        <span>www.velsa.example</span>
      </div>
    </div>

    <div class="wordmark wordmark--front">Velsa</div>

    <h1 class="headline">Lorem ipsum<br>dolor sit amet,<br>consectetur<br>adipiscing elit,<br>sed do</h1>

    <p class="offer">EXCEPTEUR SINT OCCAECAT CUPIDATAT NON<br>PROIDENT, SUNT IN CULPA QUI OFFICIA DESERUNT<br>MOLLIT ANIM ID EST LABORUM.</p>
    <div class="web-pill">WWW.VELSA.EXAMPLE</div>
  </div>
</div>
</body>
</html>
```